Book Cover for Harbor Holiday Voyage Needed!

Amber Hollow Press needs a cover for a novella. We will need an ebook cover and print wrap. We need to stay with the brand we have as indicated by the files attached. Take a look for the brand and style we are looking for.
Here are the specifics:
Title (subject to change): Starlit Passage
Subtitle: A Yuletide Novella
Series Name: The Sunny Shore Love Series (Book 3.5)
Author: Kenna Bellwood

Target Market(s)

Romance readers

Industry/Entity Type

Entertainment Industry

Font styles to use
Other font styles liked:
• NovitoNova - Title, Neumann - Subtitle

Colors
3276b5
33a6d7
33b8a4
abd036
fbee3d
ffc214

Requirements
Must have
• Please take a look at the other three covers to stay on brand and for inspiration
Nice to have
• Possibly something with a criuse ship.
Should not have
• Not looking for "real" images or depictions. We want a scene with bright colors same as the previous books but with a bit of a casual feel.

```html
<!DOCTYPE html>
<html lang="en">
<head>
<meta charset="utf-8">
<title>Starlit Passage — Book Cover</title>
<link rel="stylesheet" href="https://fonts.googleapis.com/css2?family=Big+Shoulders+Display:wght@300&family=Dancing+Script:wght@700&family=Old+Standard+TT&family=Libre+Caslon+Text&display=swap">
<style>
  :root {
    --page-bg: #3b2e27;
    --sky-top: #ee8488;
    --sky-mid: #f4aeb2;
    --sky-haze: #f3dde3;
    --horizon: #e6e6ee;
    --sea-top: #8fa9b6;
    --sea-mid: #5f97ab;
    --sea-deep: #3f8fb0;
    --ship-light: #eef0f3;
    --ship-mid: #c9ccd3;
    --ship-dark: #8e939c;
    --holly-tint: rgba(255, 255, 255, 0.32);
    --title-white: #ffffff;
    --title-shadow: #1a5775;
    --ribbon-light: #a9d6ea;
    --ribbon-dark: #7fbcd8;
    --ribbon-edge: #e8b46a;
    --ribbon-text: #c0444f;
  }
  * { margin: 0; padding: 0; box-sizing: border-box; }
  html, body {
    width: 1200px;
    height: 1200px;
    overflow: hidden;
    background: var(--page-bg);
  }
  .cover {
    position: absolute;
    left: 256px;
    top: 50px;
    width: 689px;
    height: 1100px;
    overflow: hidden;
  }
  .cover-art {
    position: absolute;
    inset: 0;
    background: linear-gradient(180deg,
      var(--sky-top) 0%,
      var(--sky-mid) 30%,
      var(--sky-haze) 60%,
      var(--horizon) 69%,
      var(--sea-top) 70%,
      var(--sea-mid) 82%,
      var(--sea-deep) 100%);
  }
  .holly-accent {
    position: absolute;
    border-radius: 50%;
    background: radial-gradient(closest-side, var(--holly-tint), rgba(255,255,255,0));
  }
  .holly-top-left     { left: 40px;  top: 86px;  width: 88px;  height: 96px; }
  .holly-top-right    { left: 424px; top: 26px;  width: 248px; height: 372px; }
  .holly-bottom-left  { left: 32px;  top: 750px; width: 96px;  height: 96px; }
  .holly-bottom-right { left: 560px; top: 710px; width: 112px; height: 200px; }
  .holly-leaf-left    { left: 56px;  top: 846px; width: 168px; height: 112px; }
  .holly-leaf-right   { left: 408px; top: 862px; width: 184px; height: 112px; }
  .ship-photo {
    position: absolute;
    left: 104px;
    top: 462px;
    width: 544px;
    height: 304px;
    border-radius: 40px 120px 60px 20px;
    background: linear-gradient(180deg, var(--ship-light) 0%, var(--ship-mid) 60%, var(--ship-dark) 100%);
    opacity: 0.85;
  }
  .series-ribbon {
    position: absolute;
    left: 136px;
    top: 100px;
    width: 412px;
    height: 40px;
    transform: rotate(-2deg);
    background: linear-gradient(180deg, var(--ribbon-light), var(--ribbon-dark));
    border-top: 2px solid var(--ribbon-edge);
    border-bottom: 2px solid var(--ribbon-edge);
    display: flex;
    align-items: center;
    justify-content: center;
  }
  .series-name {
    font-family: "Libre Caslon Text", serif;
    font-size: 20px;
    color: var(--ribbon-text);
    white-space: nowrap;
  }
  .series-number { font-size: 14px; }
  .title {
    position: absolute;
    left: 0;
    top: 0;
    width: 689px;
    height: 700px;
  }
  .title-line {
    font-family: "Big Shoulders Display", sans-serif;
    font-weight: 300;
    fill: var(--title-white);
    filter: drop-shadow(-4px 3px 0 var(--title-shadow));
  }
  .subtitle {
    position: absolute;
    left: 0;
    width: 100%;
    top: 770px;
    text-align: center;
    font-family: "Dancing Script", cursive;
    font-weight: 700;
    font-size: 50px;
    line-height: 70px;
    color: var(--title-white);
  }
  .author {
    position: absolute;
    left: 0;
    width: 100%;
    top: 970px;
    text-align: center;
    font-family: "Old Standard TT", serif;
    font-size: 44px;
    line-height: 56px;
    color: var(--title-white);
  }
</style>
</head>
<body>
  <main class="cover">
    <div class="cover-art" role="img" aria-label="Soft pink cloudy sky over a calm blue sea"></div>

    <div class="holly-accent holly-top-left" role="img" aria-label="Faint holly berries"></div>
    <div class="holly-accent holly-top-right" role="img" aria-label="Large faint holly leaves and berries"></div>
    <div class="holly-accent holly-bottom-left" role="img" aria-label="Faint holly berries"></div>
    <div class="holly-accent holly-bottom-right" role="img" aria-label="Faint holly leaves and berries"></div>
    <div class="holly-accent holly-leaf-left" role="img" aria-label="Faint holly leaf on the water"></div>
    <div class="holly-accent holly-leaf-right" role="img" aria-label="Faint holly leaf on the water"></div>

    <div class="ship-photo" role="img" aria-label="White cruise ship sailing toward the viewer on the sea"></div>

    <div class="series-ribbon">
      <span class="series-name">Sunny Shore Love Series <span class="series-number">(Book 3.5)</span></span>
    </div>

    <svg class="title" viewBox="0 0 689 700" aria-label="Starlit Passage">
      <text class="title-line" x="132" y="342" font-size="150" textLength="432" lengthAdjust="spacingAndGlyphs">STARLIT</text>
      <text class="title-line" x="132" y="622" font-size="303" textLength="432" lengthAdjust="spacingAndGlyphs">PASSAGE</text>
    </svg>

    <p class="subtitle">A Yuletide Novella...</p>
    <p class="author">KENNA BELLWOOD</p>
  </main>
</body>
</html>
```